Green Ammonia PowerPoint Slides

Hi KOV Studios. You did a PowerPoint project for us previously (As PelaGrid LLC) which we very much liked and are looking for something similar in terms of design.

VerdoMolec LLC is a project development company that develops green ammonia projects. Our concept converts renewable energy from wind, solar, hydro and geothermal power sources into ammonia which can be transported by land or sea to be used as a carbon free fuel source.

We need a professional looking design for the attached PowerPoint file. The attached PowerPoint file includes the written content for each of the slides. Designers’ final product should include all the written content and be a final product for presenting to our clients with little to no more editing required.

Designer should use the graphics attached and colors as inspiration for the design. Adjacent to the logo and where used in headings it should read: “A VerdoMolec LLC Project”. Designer is free to use/modify the logo and colors however they feel provides a more interesting design and aesthetic.

Designer should include graphics, tables and charts to better present the information where it is appropriate.

The previous design you developed for us used the ETHNOCENTRIC RG font for titles, which we liked, though you are free to use any font at your discretion as long as it is free to download.

```html
<!DOCTYPE html>
<html lang="en">
<head>
<meta charset="utf-8">
<title>VerdoMolec Green Ammonia Slides</title>
<link href="https://fonts.googleapis.com/css2?family=Audiowide&family=Open+Sans:wght@400;600;700;800&family=Oswald:wght@400&display=swap" rel="stylesheet">
<style>
:root{
  --stage:#454545;
  --navy:#0c2b52;
  --title:#143a6c;
  --blue:#2c66c6;
  --green:#6cb944;
  --green-dark:#4f9a34;
  --text:#1e1e1e;
  --link:#4caf32;
  --title-bar:#e9ebee;
}
*{box-sizing:border-box;margin:0;padding:0}
html,body{width:1200px;height:3429px;overflow:hidden;background:var(--stage)}
body{position:relative;font-family:"Open Sans",Arial,sans-serif;color:var(--text)}
.slide{position:absolute;left:62px;width:1066px;height:600px;background:#fff;overflow:hidden;box-shadow:0 4px 10px rgba(0,0,0,.35)}
.cover{top:82px;background:linear-gradient(115deg,#1a4fb0 0%,#2378b4 35%,#3fa37e 62%,#62c24e 82%,#78d045 100%)}
.cover-photo{position:absolute;inset:0;
  background:
    radial-gradient(ellipse 420px 260px at 78% 18%,rgba(220,255,200,.30),rgba(220,255,200,0) 70%),
    radial-gradient(ellipse 360px 200px at 30% 22%,rgba(160,210,255,.22),rgba(160,210,255,0) 70%),
    radial-gradient(ellipse 260px 180px at 6% 48%,rgba(8,40,90,.45),rgba(8,40,90,0) 70%),
    radial-gradient(ellipse 140px 330px at 88% 68%,rgba(30,90,40,.35),rgba(30,90,40,0) 70%),
    linear-gradient(180deg,rgba(255,255,255,0) 0%,rgba(255,255,255,.10) 44%,rgba(255,255,255,.16) 50%,rgba(0,35,90,.12) 56%,rgba(0,30,80,.38) 100%)}
.cover-mark{position:absolute;left:491px;top:120px;width:84px;height:84px;border-radius:50%;background:#fff}
.cover-title{position:absolute;left:0;right:0;top:232px;text-align:center;font-family:"Audiowide",sans-serif;color:#fff;font-size:76px;line-height:80px}
.cover-title .line2{font-size:68px}
.cover-band{position:absolute;left:191px;top:316px;width:683px;height:82px;background:var(--navy);text-align:center;font-family:"Audiowide",sans-serif;color:#fff;font-size:68px;line-height:82px}
.cover-title{top:160px}
.cover-sub{position:absolute;left:0;right:0;top:452px;text-align:center;font-family:"Audiowide",sans-serif;color:#fff;font-size:31px;letter-spacing:1px}
.cover-meta{position:absolute;left:0;right:0;top:498px;text-align:center;color:#fff;font-weight:600;font-size:22px;line-height:28px;text-decoration:underline}
.head-mark{position:absolute;left:36px;top:44px;width:58px;height:58px;border-radius:50%;background:var(--blue)}
.title-bar{position:absolute;left:108px;top:43px;width:530px;height:62px;background:linear-gradient(90deg,var(--title-bar) 60%,rgba(233,235,238,0))}
.title{position:absolute;left:120px;top:44px;font-family:"Audiowide",sans-serif;color:var(--title);font-size:51px;line-height:62px;white-space:nowrap}
.subtitle{position:absolute;left:115px;top:106px;font-family:"Audiowide",sans-serif;color:var(--title);font-size:36px}
.tag{position:absolute;right:0;top:43px;width:240px;height:32px;background:var(--green);border-radius:16px 0 0 16px;color:#fff;font-family:"Audiowide",sans-serif;font-size:18px;line-height:32px;padding-left:17px}
.footer{position:absolute;left:0;bottom:0;width:100%;height:57px;background:linear-gradient(90deg,#17467e 0%,#1f6a8a 45%,#66bb46 100%)}
.footer-url{position:absolute;left:42px;top:14px;color:#fff;font-weight:700;font-size:21px}
.page{position:absolute;right:36px;top:9px;width:40px;height:40px;border-radius:50%;background:var(--navy);color:#fff;font-weight:700;font-size:20px;line-height:40px;text-align:center}
.bullets{position:absolute;list-style:none}
.bullets li{position:relative}
.bullets li::before{content:"";position:absolute;border-radius:50%;background:linear-gradient(180deg,var(--blue) 50%,var(--green) 50%)}
.intro{left:90px;top:144px;width:925px;font-size:19.5px;line-height:23px}
.intro li{margin-bottom:22px}
.intro li::before{left:-45px;top:3px;width:24px;height:24px}
.prop{left:84px;top:178px;width:945px;font-size:15.5px;line-height:18.5px}
.prop li{margin-bottom:18px}
.prop li::before{left:-35px;top:2px;width:17px;height:17px}
.market{left:84px;top:130px;width:935px;font-size:15.5px;line-height:18.5px}
.market li{margin-bottom:16px}
.market li::before{left:-35px;top:2px;width:17px;height:17px}
.url{display:block;color:var(--link);font-family:"Oswald",sans-serif;font-size:12.5px;line-height:15px;text-decoration:underline}
.inline-url{color:var(--link);font-family:"Oswald",sans-serif;font-size:12.5px;text-decoration:underline}
.diagram{position:absolute;left:0;top:0}
.caption{position:absolute;left:0;right:0;top:3306px;text-align:center;color:#fff;font-size:32px}
</style>
</head>
<body>

<section class="slide cover" style="top:82px">
  <div class="cover-photo" role="img" aria-label="Wind turbines over a paved plaza at dusk with an engineer in a hard hat holding a tablet, tinted blue to green"></div>
  <div class="cover-mark"></div>
  <div class="cover-title">A<br><span class="line2">VERDOMOLEC LLC</span></div>
  <div class="cover-band">PROJECT</div>
  <div class="cover-sub">COVERSHEET HERE</div>
  <div class="cover-meta">Harbor Ltd - VerdoMolec Introduction<br>Date: XX/XX/XXXX</div>
</section>

<section class="slide" style="top:722px">
  <div class="head-mark"></div><div class="title-bar"></div>
  <h1 class="title">Introduction</h1>
  <div class="tag">VERDOMOLEC LLC</div>
  <ul class="bullets intro">
    <li>We are VerdoMolec, experienced energy project developers who have come together with the intent of developing opportunities in North America for the production and export of green energy.</li>
    <li>Our concept converts renewable energy; wind/solar/hydro/geothermal into ammonia, the carrier for hydrogen, which can then be transported internationally to meet the accelerating demand for green renewable power generation.</li>
    <li>We are currently in the concept development stage and are looking at ammonia export from Oregon, Alaska and Texas, and have concluded that the opportunities from Texas are preferable to those on the West Coast.</li>
    <li>We have leveraged our contacts within the LNG market and have established the necessary relationship with a key Japanese buyer who has confirmed interest in base load take off.</li>
    <li>Today we present our high-level concept for developing an ammonia export project in Texas with the goal of furthering conversations with regards your appetite for partnering.</li>
  </ul>
  <div class="footer"><span class="footer-url">WWW.PELAGRID.COM</span><span class="page">01</span></div>
</section>

<section class="slide" style="top:1363px">
  <div class="head-mark"></div><div class="title-bar"></div>
  <h1 class="title">The Proposition</h1>
  <h2 class="subtitle">Why Hydrogen and Green Ammonia?</h2>
  <div class="tag">VERDOMOLEC LLC</div>
  <ul class="bullets prop">
    <li><b>It's unique</b> - Hydrogen is the only fully renewable fuel by which large quantities of energy can be efficiently transported internationally.</li>
    <li><b>It has a proven safety record</b> - While hydrogen has inherent safety issue, synthesis with nitrogen into ammonia enables transport via the established international network of large ocean-going bulk carriers.</li>
    <li><b>It's green</b> - When Ammonia is re-converted back into electricity via thermal power production there is no CO2 released, catalyst technologies will mean only nitrogen and water are emitted.</li>
    <li><b>The color difference</b> – Grey ammonia is currently produced using hydrogen derived from natural gas, blue ammonia is grey ammonia with carbon sequestration added, neither are green or sustainable. Green Ammonia utilizes renewable electricity to produce hydrogen via electrolysis, this is then combined with nitrogen produced from air via liquefaction. The only emission is oxygen, also a valuable bi-product.</li>
    <li><b>Its power friendly</b> – Ammonia synthesis requires low power as the exothermic reaction generates steam which in turn generates power to run the ammonia facility.</li>
    <li><b>Technology readiness</b> – Industrial scale modular electrolizers are market ready.</li>
  </ul>
  <div class="footer"><span class="footer-url">WWW.PELAGRID.COM</span><span class="page">02</span></div>
</section>

<section class="slide" style="top:2004px">
  <div class="head-mark"></div><div class="title-bar" style="width:640px"></div>
  <h1 class="title" style="font-size:44px">Project Block Flow Diagram</h1>
  <div class="tag">VERDOMOLEC LLC</div>
  <svg class="diagram" width="1066" height="543" viewBox="0 0 1066 543" font-family="Open Sans, sans-serif">
    <defs>
      <marker id="arrow" markerWidth="8" markerHeight="8" refX="6" refY="4" orient="auto"><path d="M0,0 L8,4 L0,8 z" fill="#2c66c6"/></marker>
      <polygon id="hex" points="0,-44 38,-22 38,22 0,44 -38,22 -38,-22"/>
    </defs>
    <g font-size="10.5" font-weight="700" fill="#222" text-anchor="middle">
      <text x="134" y="187">~240MW+</text>
      <text x="134" y="410">~XXX</text><text x="134" y="422">Gallons/Day</text>
      <text x="262" y="410">~XXX</text><text x="262" y="422">Gallons/Day</text>
      <text x="805" y="204">~6800m³ NH3</text>
      <text x="805" y="224">Storage (~7 days</text><text x="805" y="236">production)</text>
      <text x="958" y="382">~XXXm³</text><text x="958" y="394">(Customer</text><text x="958" y="406">Determined)</text>
      <text x="420" y="362">12 x ~20MW</text>
    </g>
    <text x="546" y="180" text-anchor="middle" font-size="21" font-weight="800" fill="#111">~600 Te/Day NH3</text>
    <text x="546" y="199" text-anchor="middle" font-size="13" fill="#333">~576,000m³/day O2</text>
    <rect x="207" y="213" width="679" height="163" fill="none" stroke="#2c66c6" stroke-width="1.3" stroke-dasharray="4 3"/>
    <polygon points="339,225 715,225 715,214 741,240 715,266 715,255 339,255" fill="#2c66c6"/>
    <text x="518" y="245" text-anchor="middle" font-size="12" font-weight="700" fill="#fff">Ammonia Production Unit</text>
    <g fill="#6cb944" stroke="#4f9a34"><rect x="339" y="266" width="121" height="81"/><rect x="467" y="266" width="121" height="81"/><rect x="594" y="266" width="122" height="81"/></g>
    <g font-size="11" font-weight="600" fill="#fff" text-anchor="middle">
      <text x="400" y="303">HYDROLYSIS</text><text x="400" y="316">UNITS</text>
      <text x="527" y="303">AIR SEPARATION</text><text x="527" y="316">UNIT</text>
      <text x="655" y="303">SYNTHESIS</text><text x="655" y="316">UNIT</text>
    </g>
    <g fill="#6cb944" stroke="#4f9a34" stroke-width="1.5">
      <use href="#hex" x="134" y="237"/><use href="#hex" x="134" y="350"/><use href="#hex" x="262" y="343"/>
      <use href="#hex" x="805" y="303"/><use href="#hex" x="958" y="303"/>
    </g>
    <g font-size="10" font-weight="600" fill="#fff" text-anchor="middle">
      <text x="134" y="228">RENEWABLE</text><text x="134" y="240">POWER</text>
      <path d="M136,246 L128,260 L134,260 L131,272 L140,256 L134,256 z" fill="#fff"/>
      <text x="134" y="339">FEED</text><text x="134" y="351">WATER</text>
      <path d="M134,356 C128,366 128,372 134,372 C140,372 140,366 134,356 z" fill="#fff"/>
      <g font-size="8.5"><text x="262" y="330">WATER</text><text x="262" y="341">CONDITIONING</text><text x="262" y="352">&amp;</text><text x="262" y="363">PURIFICATION</text></g>
      <text x="805" y="297">STORAGE &amp;</text><text x="805" y="309">LOADING</text>
      <text x="805" y="325" font-size="8">NH3 TANK</text>
      <text x="958" y="286">AMMONIA</text><text x="958" y="298">TRANSPORT</text><text x="958" y="310">VESSEL</text>
      <path d="M946,318 h24 l-4,8 h-16 z" fill="#fff"/>
    </g>
    <g stroke="#2c66c6" stroke-width="3" marker-end="url(#arrow)">
      <line x1="174" y1="278" x2="332" y2="278"/>
      <line x1="173" y1="343" x2="215" y2="343"/>
      <line x1="301" y1="343" x2="332" y2="343"/>
      <line x1="716" y1="307" x2="759" y2="307"/>
      <line x1="845" y1="307" x2="912" y2="307"/>
      <line x1="536" y1="432" x2="536" y2="388"/>
    </g>
    <rect x="394" y="434" width="287" height="56" fill="#fff" stroke="#2c66c6" stroke-width="1.3" stroke-dasharray="4 3"/>
    <text x="537" y="458" text-anchor="middle" font-size="11" font-weight="600" fill="#222">Facility footprint including expansion to</text>
    <text x="537" y="472" text-anchor="middle" font-size="11" font-weight="600" fill="#222">1200 Te/Day ~XXX-XXX Acres</text>
  </svg>
  <div class="footer"><span class="footer-url">WWW.PELAGRID.COM</span><span class="page">03</span></div>
</section>

<section class="slide" style="top:2646px">
  <div class="head-mark"></div><div class="title-bar"></div>
  <h1 class="title">Is There a Market?</h1>
  <div class="tag">VERDOMOLEC LLC</div>
  <ul class="bullets market">
    <li>The key driver is the Paris Climate Agreement which requires global commitments to carbon neutrality by 2050.</li>
    <li>Japan is one of 129 countries that have committed to achieve the Paris Climate Agreement. They need to do so without base load nuclear which remains impacted by Fukashima. Kestrel Advisory and others have assessed that green ammonia will have to become a major component of Japan's energy supply to achieve that commitment.
      <span class="url">https://www.kestreladvisory.com/insights/sustainability/how-japan-could-reach-carbon-neutrality-by-2050</span></li>
    <li>Japan's major power supplier has announced plans for a coal transition to ammonia commencing with 20% co-firing in 2024 which will ramp up nationally over the following decade and eventually to a full transition to Ammonia in early 2040's. Japan has stated it will require 30MM Te per annum of green ammonia, the equivalent of 30 world scale ammonia production facilities that will require 34GW of renewable electricity.
      <span class="url">https://www.fuelmarketwatch.com/news/coal/020821-japan-sees-30-mil-mtyear-fuel-ammonia-demand-in-2050-after-commercial-use-in-2020s</span></li>
    <li>Hoshiro Heavy have announced the worlds first 40MW ammonia fired gas turbine with an availability date of 2025. Other gas turbine suppliers will match that announcement shortly. <span class="inline-url">https://power.hoshiro.com/news/20210301.html</span></li>
    <li>Green Ammonia requires 3 industrial scale processes, green generation, electrolysis and ammonia synthesis. There is acknowledgment that this will not facilitate direct competition with grey and blue ammonia on price. That said, the price needs to be transparent for a market to develop and with transparency comes competition to combine the 3 industrial process. We believe Texas is positioned to deliver efficiently and effectively.
      <span class="url">https://www.ammoniaoutlook.org/articles/the-cost-of-co2-free-ammonia/</span></li>
  </ul>
  <div class="footer"><span class="footer-url">WWW.PELAGRID.COM</span><span class="page">04</span></div>
</section>

<p class="caption">Green Ammonia PowerPoint Slides</p>
</body>
</html>
```